Volora Laundry and Dry Cleaning Poster

We need a Poster and Window Sticker for our Laundry and Dry cleaning shop (VOLORA LAUNDRY AND DRY CLEANING).
info we like on the design. Logo is included
Company Name: Volora Laundry and Dry Cleaning
Slogan: It Comes Back Clean
Location: Kwentu-Dasor, Accra
Working Hours: Mon-Sat 8am to 5pm
Tel: +233 30 781 6242
email:info@voloralaundry.example
website: www.voloralaundry.example
fb: fb.com/voloralaundry

Target Market(s)

Laundry Shop

Colors
33a6d7
9bcb3b

```html
<!DOCTYPE html>
<html lang="en">
<head>
<meta charset="utf-8">
<title>Volora Laundry and Dry Cleaning Poster</title>
<link href="https://fonts.googleapis.com/css2?family=Ubuntu:wght@500;700&family=Exo+2:ital,wght@1,900&display=swap" rel="stylesheet">
<style>
  :root {
    --frame: #000000;
    --sky: #33a6d7;
    --sky-deep: #2590c9;
    --sky-light: #5fd8f0;
    --aqua: #8ff0fa;
    --lime: #9bcb3b;
    --lime-deep: #6fae1f;
    --ink-blue: #2a8fcf;
    --outline-blue: #2f8fd0;
    --white: #ffffff;
  }
  html, body {
    margin: 0;
    padding: 0;
    width: 1200px;
    height: 1019px;
    overflow: hidden;
    background: var(--frame);
  }
  .poster {
    position: absolute;
    left: 88px;
    top: 75px;
    width: 1024px;
    height: 868px;
    overflow: hidden;
    background: radial-gradient(ellipse 700px 520px at 520px 420px, var(--sky-light) 0%, var(--sky) 65%, var(--sky-deep) 100%);
    font-family: "Ubuntu", Arial, sans-serif;
  }
  .bubble-scene {
    position: absolute;
    left: 0;
    top: 0;
    width: 1024px;
    height: 868px;
    background: radial-gradient(circle 345px at 530px 440px,
      var(--white) 0%, var(--white) 82%,
      #c9f1fb 86%, var(--sky) 92%, var(--aqua) 97%, rgba(143,240,250,0) 100%);
  }
  .brand {
    position: absolute;
    left: 0;
    width: 1034px;
    top: 234px;
    text-align: center;
  }
  .brand-mark {
    display: inline-flex;
    align-items: center;
    gap: 12px;
    font-weight: 700;
    font-size: 56px;
    line-height: 1;
    color: var(--ink-blue);
  }
  .brand-dot {
    width: 48px;
    height: 48px;
    border-radius: 50%;
    background: var(--lime-deep);
  }
  .brand-sub {
    margin-top: 4px;
    padding-left: 70px;
    font-size: 10px;
    font-weight: 700;
    letter-spacing: 0.4px;
    color: var(--lime-deep);
  }
  .company-name {
    position: absolute;
    left: 0;
    width: 1034px;
    top: 325px;
    text-align: center;
    font-size: 26px;
    font-weight: 700;
    color: var(--ink-blue);
  }
  .slogan {
    position: absolute;
    left: 0;
    top: 0;
    margin: 0;
  }
  .slogan text {
    font-family: "Exo 2", "Arial Black", sans-serif;
    font-style: italic;
    font-weight: 900;
    font-size: 98px;
    letter-spacing: -2px;
    text-anchor: middle;
    stroke-linejoin: round;
  }
  .slogan .outline { fill: var(--outline-blue); stroke: var(--outline-blue); stroke-width: 14px; }
  .slogan .inline { fill: var(--white); stroke: var(--white); stroke-width: 6px; }
  .slogan .face { fill: var(--lime); }
  .details {
    position: absolute;
    left: 360px;
    top: 543px;
    margin: 0;
    padding: 0;
    list-style: none;
    font-size: 27px;
    font-weight: 700;
    color: var(--ink-blue);
    line-height: 29px;
  }
  .details li {
    display: flex;
    align-items: center;
    gap: 4px;
  }
  .details svg { flex: none; }
  .contacts {
    position: absolute;
    left: 70px;
    top: 794px;
    display: flex;
    gap: 14px;
  }
  .contact {
    display: flex;
    align-items: center;
    gap: 4px;
    padding: 2px 8px;
    background: rgba(37,144,201,0.55);
    font-size: 20px;
    font-weight: 700;
    color: var(--white);
  }
</style>
</head>
<body>
<main class="poster">

  <div class="bubble-scene" role="img" aria-label="Soap bubbles floating around a round white badge with a blue ring"></div>

  <div class="brand">
    <div class="brand-mark"><span class="brand-dot"></span>Volora</div>
    <div class="brand-sub">LAUNDRY AND DRY CLEANING</div>
  </div>

  <div class="company-name">Volora Laundry and Dry Cleaning</div>

  <h1 class="slogan" aria-label="It comes back clean">
    <svg width="1024" height="868" viewBox="0 0 1024 868" aria-hidden="true">
      <g class="outline">
        <text x="517" y="446">IT COMES</text>
        <text x="524" y="526">BACK CLEAN</text>
      </g>
      <g class="inline">
        <text x="517" y="446">IT COMES</text>
        <text x="524" y="526">BACK CLEAN</text>
      </g>
      <g class="face">
        <text x="517" y="446">IT COMES</text>
        <text x="524" y="526">BACK CLEAN</text>
      </g>
    </svg>
  </h1>

  <ul class="details">
    <li>
      <svg width="22" height="22" viewBox="0 0 22 22" aria-hidden="true"><circle cx="11" cy="11" r="9" fill="none" stroke="#6fae1f" stroke-width="3"/><path d="M11 6v5l4 2" stroke="#6fae1f" stroke-width="2.5" fill="none"/></svg>
      <span>: Mon-Sat 8am to 5pm</span>
    </li>
    <li>
      <svg width="22" height="24" viewBox="0 0 22 24" aria-hidden="true"><path d="M11 2a7 7 0 0 1 7 7c0 5-7 13-7 13S4 14 4 9a7 7 0 0 1 7-7z" fill="#6fae1f"/><circle cx="11" cy="9" r="2.6" fill="#fff"/></svg>
      <span>: Kwentu-Dasor, Accra</span>
    </li>
    <li>
      <svg width="22" height="24" viewBox="0 0 22 24" aria-hidden="true"><path d="M6 3l4 4-2 3c1 3 3 5 6 6l3-2 4 4-3 3C9 21 2 12 3 6z" fill="#6fae1f"/></svg>
      <span>: +233 30 781 6242</span>
    </li>
  </ul>

  <div class="contacts">
    <div class="contact">
      <svg width="18" height="14" viewBox="0 0 18 14" aria-hidden="true"><rect x="1" y="1" width="16" height="12" fill="#9bcb3b"/><path d="M1 1l8 7 8-7" stroke="#2590c9" stroke-width="1.5" fill="none"/></svg>
      <span>: info@voloralaundry.example</span>
    </div>
    <div class="contact">
      <svg width="18" height="18" viewBox="0 0 18 18" aria-hidden="true"><g fill="none" stroke="#9bcb3b" stroke-width="1.6"><circle cx="9" cy="9" r="7.5"/><ellipse cx="9" cy="9" rx="3.5" ry="7.5"/><path d="M1.5 9h15"/></g></svg>
      <span>: www.voloralaundry.example</span>
    </div>
    <div class="contact">
      <svg width="18" height="18" viewBox="0 0 18 18" aria-hidden="true"><rect x="1" y="1" width="16" height="16" fill="#9bcb3b"/></svg>
      <span>: fb.com/voloralaundry</span>
    </div>
  </div>

</main>
</body>
</html>
```